Book Cover on Entrepreneurship for Eye Doctors

Book Title: The Lens Clinic Founder: How to launch your practice with flair
Author: Morvan Tessaleq, Optom, MBA, DBA, EIC
I need a Book Cover with the following descriptions:
Topic: the book topic is entrepreneurship knowledge for eye care professionals.
The book's audience: eye care professionals who you know as Opticians, who sell eyeglasses and sunglasses;
Optometrists, test eyes, fit contact lenses, and prescribe medication
Ophthalmologists, perform eye surgery
More about the audience:
1- Young eye care professionals who don’t know about entrepreneurship and those who are stuck in the 9-to-5 job;
2- This is the first book written on entrepreneurship with eye care professionals in mind.
3- Private practice owners the established business guys who are looking to grow their business;
4- Many eye care professionals are MBA holders they may have learned a little bit about entrepreneurship during their MBA studies.
Use the sample cover above and the suggestions that follow as a guide:
1- The cover should be very simple leaving an empty space somewhere to sign the book;
2- The Title and author name should use a modern font;
3- The cover should provide info about what's inside the book through illustrations, for example:
a- Gears: illustrating entrepreneur growth mindset (or anything more explicit)
b- Spectacles, sunglasses, lenses, eye drops, or any other eye care-related correction tools illustrating eye care (or anything more explicit)
c- Symbols illustrating ideas, opportunity, and profit, like money, charts, light bulbs, brain, and coins,...(or anything more explicit)
d- Entrepreneurship illustrated by Briefcase, tie, suit,... (or anything more explicit)

The rest is your creativity and imagination interplay.

Target Market(s)

Eye care professionals: Opticians, Optometrists, Ophthalmologists, Eye Care Administrators, Students in eye specialties.

Industry/Entity Type

eye care

Requirements
Must have
• 1- The cover should be very simple leaving an empty space somewhere to sign the book; 2- The Title and author name should use a modern font; 3- The cover should provide info about what's inside the book through illustrations, for example: a- Gears: illustrating entrepreneur growth mindset (or anything more explicit) b- Spectacles, sunglasses, lenses, eye drops, or any other eye care-related correction tools illustrating eye care (or anything more explicit) c- Symbols illustrating ideas, opportunity, and profit, like money, charts, light bulbs, brain, and coins,...(or anything more explicit) d- Entrepreneurship illustrated by Briefcase, tie, suit,... (or anything more explicit)

```html
<!DOCTYPE html>
<html lang="en">
<head>
<meta charset="utf-8">
<title>The Lens Clinic Founder — Book Cover</title>
<link rel="stylesheet" href="https://fonts.googleapis.com/css2?family=Bebas+Neue&family=Poppins:wght@500;600&family=Oswald:wght@500;600&display=swap">
<style>
  :root {
    --page-bg: #ffffff;
    --cover-bg: #d3e4e6;
    --title-blue: #1f4ea0;
    --ink: #222325;
    --ink-soft: #4a4d50;
    --rule-blue: #1f4ea0;
  }
  * { margin: 0; padding: 0; box-sizing: border-box; }
  html, body {
    width: 1200px;
    height: 1000px;
    overflow: hidden;
    background: var(--page-bg);
  }
  .canvas {
    position: relative;
    width: 1200px;
    height: 1000px;
  }
  .cover {
    position: absolute;
    left: 296px;
    top: 50px;
    width: 607px;
    height: 900px;
    background: var(--cover-bg);
    color: var(--ink);
    overflow: hidden;
  }
  .title-kicker {
    position: absolute;
    top: 54px;
    left: 0;
    width: 100%;
    display: flex;
    align-items: center;
    justify-content: center;
    gap: 22px;
  }
  .title-kicker .kicker-rule {
    width: 130px;
    height: 3px;
    background: var(--ink);
  }
  .title-kicker .kicker-word {
    font-family: "Bebas Neue", sans-serif;
    font-size: 52px;
    line-height: 1;
    letter-spacing: 0.04em;
    color: var(--ink);
  }
  .title-main {
    position: absolute;
    left: 0;
    width: 100%;
    text-align: center;
    font-family: "Bebas Neue", sans-serif;
    line-height: 1;
    letter-spacing: 0.005em;
  }
  .title-main--blue {
    top: 100px;
    font-size: 124px;
    color: var(--title-blue);
  }
  .title-main--dark {
    top: 205px;
    font-size: 114px;
    color: var(--ink);
  }
  .chart-row {
    position: absolute;
    left: 0;
    width: 100%;
    height: 80px;
    display: flex;
    align-items: center;
    justify-content: center;
  }
  .chart-row .chart-text {
    font-family: "Poppins", sans-serif;
    font-weight: 600;
    line-height: 1;
    color: var(--ink);
    white-space: nowrap;
  }
  .chart-row .chart-mark {
    position: absolute;
    left: 46px;
    top: 50%;
    transform: translateY(-50%);
    font-family: "Poppins", sans-serif;
    font-weight: 500;
    font-size: 9px;
    color: var(--ink-soft);
    letter-spacing: 0.02em;
  }
  .chart-row .chart-line-no {
    position: absolute;
    right: 50px;
    top: 50%;
    transform: translateY(-50%);
    font-family: "Poppins", sans-serif;
    font-weight: 500;
    font-size: 13px;
    color: var(--ink-soft);
  }
  .chart-row--1 { top: 373px; }
  .chart-row--1 .chart-text { font-size: 68px; letter-spacing: 0.3em; margin-right: -0.3em; }
  .chart-row--2 { top: 481px; }
  .chart-row--2 .chart-text { font-size: 58px; letter-spacing: 0.38em; margin-right: -0.38em; }
  .chart-row--3 { top: 574px; }
  .chart-row--3 .chart-text { font-size: 38px; letter-spacing: 0.1em; margin-right: -0.1em; }
  .chart-row--4 { top: 662px; }
  .chart-row--4 .chart-text { font-size: 32px; letter-spacing: 0.12em; margin-right: -0.12em; }
  .closing-rule {
    position: absolute;
    top: 777px;
    left: 98px;
    width: 411px;
    height: 4px;
    background: var(--rule-blue);
  }
  .author-line {
    position: absolute;
    top: 844px;
    left: 0;
    width: 100%;
    text-align: center;
    font-family: "Oswald", sans-serif;
    font-weight: 600;
    font-size: 25px;
    line-height: 1;
    letter-spacing: 0.1em;
    color: var(--ink);
  }
</style>
</head>
<body>
  <main class="canvas">
    <section class="cover" aria-label="Book cover: The Lens Clinic Founder">
      <header>
        <div class="title-kicker">
          <span class="kicker-rule"></span>
          <span class="kicker-word">THE</span>
          <span class="kicker-rule"></span>
        </div>
        <h1>
          <span class="title-main title-main--blue">LENS CLINIC</span>
          <span class="title-main title-main--dark">FOUNDER</span>
        </h1>
      </header>

      <div class="chart-row chart-row--1">
        <span class="chart-mark">20/200</span>
        <span class="chart-text">HOW TO</span>
        <span class="chart-line-no">1</span>
      </div>
      <div class="chart-row chart-row--2">
        <span class="chart-mark">20/100</span>
        <span class="chart-text">LAUNCH</span>
        <span class="chart-line-no">2</span>
      </div>
      <div class="chart-row chart-row--3">
        <span class="chart-mark">20/70</span>
        <span class="chart-text">YOUR PRACTICE</span>
        <span class="chart-line-no">3</span>
      </div>
      <div class="chart-row chart-row--4">
        <span class="chart-mark">20/50</span>
        <span class="chart-text">WITH FLAIR</span>
        <span class="chart-line-no">4</span>
      </div>

      <div class="closing-rule"></div>

      <p class="author-line">MORVAN TESSALEQ, OPTOM, MBA, DBA, EIC</p>
    </section>
  </main>
</body>
</html>
```